Italian Restaurant
Stationary
Project: Italian Restaurant
Italian Restaurant - Food
Creative Brief
Modern
Dale Morrow
Owner
4186 Larkspur Avenue Winter Park, FL 32795
castellinos@mailvane.com
castellinos-example.com

```html
<!DOCTYPE html>
<html lang="en">
<head>
<meta charset="utf-8">
<title>Castellino's – Business Cards</title>
<link href="https://fonts.googleapis.com/css2?family=Arimo:wght@400;700&display=swap" rel="stylesheet">
<style>
  :root{
    --backdrop:#ecebe8;
    --card:#ffffff;
    --wine:#8e1b1b;
    --wine-dark:#6a1010;
    --gold:#c9a227;
    --ink:#555555;
    --rule:#cfcfcf;
  }
  *{margin:0;padding:0;box-sizing:border-box}
  html,body{width:1200px;height:852px;overflow:hidden}
  body{background:var(--backdrop);font-family:"Arimo",Arial,sans-serif;position:relative}
  .card{
    position:absolute;width:540px;height:310px;background:var(--card);
    border-radius:22px;box-shadow:0 6px 18px rgba(0,0,0,.18);
  }
  .card--front{left:50px;top:90px}
  .card--back{left:610px;top:452px}
  .edge-tab{
    position:absolute;top:124px;width:12px;height:62px;
    background:linear-gradient(90deg,var(--wine-dark),var(--wine));
  }
  .edge-tab--left{left:0;border-radius:0 6px 6px 0}
  .edge-tab--right{right:0;border-radius:6px 0 0 6px}
  .brand{
    position:absolute;display:flex;align-items:center;gap:10px;
    font-weight:700;font-size:34px;color:var(--wine);letter-spacing:.3px;white-space:nowrap;
  }
  .brand-dot{width:20px;height:20px;border-radius:50%;background:var(--gold);flex:none}
  .card--front .brand{left:155px;top:62px}
  .card--back .brand{left:34px;top:136px}
  .person{position:absolute}
  .person-name{font-weight:700;font-size:18px;color:var(--wine)}
  .person-role{font-size:14px;color:var(--gold);margin-top:2px}
  .address{font-size:13px;color:var(--ink);line-height:1.35}
  .card--front .person{right:290px;top:172px;text-align:right}
  .card--front .address{position:absolute;right:290px;top:232px;text-align:right}
  .card--back .person{left:312px;top:42px}
  .card--back .address{position:absolute;left:312px;top:100px}
  .divider{position:absolute;width:1px;background:var(--rule)}
  .card--front .divider{left:264px;top:160px;height:120px}
  .card--back .divider{left:294px;top:36px;height:240px}
  .contacts{position:absolute;list-style:none;font-size:13px;color:var(--ink)}
  .contacts li{display:flex;align-items:center;gap:7px;height:20px}
  .contacts svg{width:13px;height:13px;flex:none;fill:var(--wine)}
  .card--front .contacts{left:278px;top:164px}
  .card--back .contacts{left:312px;top:152px}
</style>
</head>
<body>
<svg width="0" height="0" style="position:absolute">
  <defs>
    <symbol id="icon-phone" viewBox="0 0 16 16"><path d="M3 1h3l1.5 4-2 1.2a9 9 0 0 0 4.3 4.3L11 8.5 15 10v3a2 2 0 0 1-2 2C6.4 15 1 9.6 1 3a2 2 0 0 1 2-2z"/></symbol>
    <symbol id="icon-mobile" viewBox="0 0 16 16"><path d="M4 0h8a1 1 0 0 1 1 1v14a1 1 0 0 1-1 1H4a1 1 0 0 1-1-1V1a1 1 0 0 1 1-1zm1 2v10h6V2zm3 11a1 1 0 1 0 0 2 1 1 0 0 0 0-2z"/></symbol>
    <symbol id="icon-fax" viewBox="0 0 16 16"><path d="M4 0h6l2 2v4H4zM1 7h14v7H1zm3 2v2h8V9z"/></symbol>
    <symbol id="icon-mail" viewBox="0 0 16 16"><path d="M1 3h14v10H1zm1.5 1.2L8 8.5l5.5-4.3z"/></symbol>
    <symbol id="icon-web" viewBox="0 0 16 16"><circle cx="8" cy="8" r="7"/></symbol>
  </defs>
</svg>

<article class="card card--front">
  <span class="edge-tab edge-tab--left"></span>
  <span class="edge-tab edge-tab--right"></span>
  <div class="brand"><span class="brand-dot"></span>Castellino's</div>
  <div class="person">
    <div class="person-name">Dale Morrow</div>
    <div class="person-role">Owner</div>
  </div>
  <p class="address">4186 Larkspur Avenue<br>Winter Park, FL 32795</p>
  <span class="divider"></span>
  <ul class="contacts">
    <li><svg><use href="#icon-phone"/></svg>(407) 555-0148</li>
    <li><svg><use href="#icon-mobile"/></svg>(630) 555-0192</li>
    <li><svg><use href="#icon-fax"/></svg>(407) 555-0163</li>
    <li><svg><use href="#icon-mail"/></svg>castellinos@mailvane.com</li>
    <li><svg><use href="#icon-web"/></svg>castellinos-example.com</li>
  </ul>
</article>

<article class="card card--back">
  <span class="edge-tab edge-tab--left"></span>
  <span class="edge-tab edge-tab--right"></span>
  <div class="brand"><span class="brand-dot"></span>Castellino's</div>
  <span class="divider"></span>
  <div class="person">
    <div class="person-name">Dale Morrow</div>
    <div class="person-role">Owner</div>
  </div>
  <p class="address">4186 Larkspur Avenue<br>Winter Park, FL 32795</p>
  <ul class="contacts">
    <li><svg><use href="#icon-phone"/></svg>(407) 555-0148</li>
    <li><svg><use href="#icon-mobile"/></svg>(630) 555-0192</li>
    <li><svg><use href="#icon-fax"/></svg>(407) 555-0163</li>
    <li><svg><use href="#icon-mail"/></svg>castellinos@mailvane.com</li>
    <li><svg><use href="#icon-web"/></svg>castellinos-example.com</li>
  </ul>
</article>
</body>
</html>
```